Local Roofing/Construction company business needs new biz card design

We need a new business card design, current cards are from the start of this operation and generic at best. We are a local Construction Company (General Contractor) with a majority of our work originating from insurance claims-exterior finish work is the main focus (Roofs-Siding-Gutters etc). Heavily involved with homeowners and the low ball offers they receive from insurance company's after a insurable event takes place. I have attached some of our original logo file(s) below.

```html
<!DOCTYPE html>
<html lang="en">
<head>
<meta charset="utf-8">
<title>Stonecrest Construction – Business Card</title>
<link rel="stylesheet" href="https://fonts.googleapis.com/css2?family=Lato:wght@400;700;900&display=swap">
<style>
  :root {
    --page-bg: #2a2d2f;
    --card-bg: #0e1e21;
    --card-pattern: #11262a;
    --accent: #2ee07a;
    --text-light: #e9efee;
    --text-soft: #c9d3d1;
  }
  * { margin: 0; padding: 0; box-sizing: border-box; }
  html, body { width: 1200px; height: 952px; overflow: hidden; }
  body {
    background: var(--page-bg);
    font-family: "Lato", sans-serif;
    position: relative;
  }
  .card {
    position: absolute;
    left: 250px;
    width: 700px;
    height: 400px;
    border-radius: 28px;
    background: var(--card-bg);
    overflow: hidden;
    box-shadow: 0 10px 30px rgba(0,0,0,.45);
  }
  .card--front { top: 60px; }
  .card--back { top: 492px; }

  .brand {
    position: absolute;
    left: 52px;
    top: 46px;
    display: flex;
    align-items: center;
    gap: 12px;
  }
  .brand__mark {
    width: 22px; height: 22px;
    background: var(--accent);
    border-radius: 4px;
  }
  .brand__name {
    color: var(--accent);
    font-weight: 900;
    font-size: 26px;
    letter-spacing: 1px;
    text-transform: uppercase;
    line-height: 1.1;
  }

  .contact {
    position: absolute;
    left: 52px;
    top: 150px;
    list-style: none;
  }
  .contact__item {
    display: flex;
    align-items: flex-start;
    gap: 12px;
    color: var(--text-light);
    font-size: 15px;
    line-height: 1.35;
    margin-bottom: 12px;
  }
  .contact__icon {
    flex: none;
    width: 20px; height: 20px;
    border-radius: 4px;
    background: var(--text-light);
    display: flex; align-items: center; justify-content: center;
  }
  .contact__icon--pin { background: var(--accent); }

  .person {
    position: absolute;
    right: 56px;
    top: 178px;
    text-align: right;
  }
  .person__name {
    font-size: 30px;
    font-weight: 400;
    color: var(--text-light);
    letter-spacing: 1.5px;
    text-transform: uppercase;
  }
  .person__surname { color: var(--accent); font-weight: 900; }
  .person__role {
    font-size: 19px;
    color: var(--text-soft);
    margin-top: 4px;
    letter-spacing: .5px;
  }

  .back-pattern {
    position: absolute; inset: 0;
    background: var(--card-pattern);
  }
  .back-brand {
    position: absolute;
    left: 50%; top: 50%;
    transform: translate(-50%, -50%);
    display: flex; align-items: center; gap: 14px;
  }
  .back-brand .brand__mark { width: 26px; height: 26px; }
  .back-brand .brand__name { font-size: 30px; }
</style>
</head>
<body>

<section class="card card--front" aria-label="Business card front">
  <div class="brand">
    <span class="brand__mark"></span>
    <span class="brand__name">Stonecrest<br>Construction</span>
  </div>

  <ul class="contact">
    <li class="contact__item">
      <span class="contact__icon contact__icon--pin">
        <svg width="12" height="14" viewBox="0 0 12 14"><path d="M6 0a5 5 0 0 0-5 5c0 4 5 9 5 9s5-5 5-9a5 5 0 0 0-5-5zm0 7a2 2 0 1 1 0-4 2 2 0 0 1 0 4z" fill="#0e1e21"/></svg>
      </span>
      <span>712 Alder Ridge Road<br>Fairview, OH 44126</span>
    </li>
    <li class="contact__item">
      <span class="contact__icon">
        <svg width="12" height="12" viewBox="0 0 12 12"><path d="M2.5 0.5l2 2.5-1.2 1.3a7 7 0 0 0 4.4 4.4L9 7.5l2.5 2-1.3 2C5 11.5 0.5 7 0.5 1.8z" fill="#0e1e21"/></svg>
      </span>
      <span>+1 440 555 0173</span>
    </li>
    <li class="contact__item">
      <span class="contact__icon">
        <svg width="13" height="10" viewBox="0 0 13 10"><rect x="0.5" y="0.5" width="12" height="9" fill="none" stroke="#0e1e21" stroke-width="1.3"/><path d="M0.5 0.5l6 5 6-5" fill="none" stroke="#0e1e21" stroke-width="1.3"/></svg>
      </span>
      <span>office@stonecrestbuild.com</span>
    </li>
    <li class="contact__item">
      <span class="contact__icon">
        <svg width="12" height="12" viewBox="0 0 12 12"><circle cx="6" cy="6" r="5" fill="none" stroke="#0e1e21" stroke-width="1.3"/><path d="M1 6h10M6 1c2 2.5 2 7.5 0 10M6 1c-2 2.5-2 7.5 0 10" fill="none" stroke="#0e1e21" stroke-width="1"/></svg>
      </span>
      <span>www.stonecrestbuild.com</span>
    </li>
  </ul>

  <div class="person">
    <p class="person__name">Daniel M. <span class="person__surname">Harlow</span></p>
    <p class="person__role">General Contractor</p>
  </div>
</section>

<section class="card card--back" aria-label="Business card back">
  <div class="back-pattern" role="img" aria-label="Tonal repeating brand pattern across the card"></div>
  <div class="back-brand">
    <span class="brand__mark"></span>
    <span class="brand__name">Stonecrest Construction</span>
  </div>
</section>

</body>
</html>
```